High End Personalized Functional Medicine in Women's Health

We are adding new and exciting personalized medicine services to our Women's Health Care practice focusing on health optimization and anti-aging as well as hormone replacement therapy and need a high end brochure to educate patients about these services. We would like to see a zen-like design that has feminine appeal. Our office colors are vibrant but soothing. We have utilized the concepts of feng shui to optimize our positive energy. The exterior of the building is peach and cream and these colors would blend with that energy The final design should communicate a sense that you can take control of your health and aging.

Target Market(s)

Females age 35-65 with annual income >$75000/year

Industry/Entity Type

Health And Wellness

Logo Text

Bright Path is the company name. Our sister company is Corva Ridge Ob/Gyn

Font styles to use
Serif

Colors

Designer to choose colors to be used in the design.

Requirements
Must have
• My project must have clean lines. I like a strong feminine appearance, not a fluffy curvy feminine look. Professional appearance, Brochure would be on thicker card stock. A strong front page that makes you want to open the brochure
Nice to have
• Eye catching photos that complement our message . I am not tied to the peach and cream color recommendation, but find those colors feminine but not so cliche as pinks and purples.
Should not have
• frilly design

```html
<!DOCTYPE html>
<html lang="en">
<head>
<meta charset="utf-8">
<title>Bright Path Brochure Cover</title>
<link href="https://fonts.googleapis.com/css2?family=Cormorant+Garamond:wght@400&display=swap" rel="stylesheet">
<style>
  :root {
    --backdrop: #d6d6d6;
    --paper: #ffffff;
    --peach-line: #ecdccb;
    --peach: #e3c4ab;
    --taupe: #c4bdb3;
    --stone-light: #efece6;
    --stone-mid: #d9d3c9;
  }
  html, body {
    margin: 0;
    padding: 0;
    width: 1200px;
    height: 900px;
    overflow: hidden;
    background: var(--backdrop);
  }
  .cover {
    position: absolute;
    left: 100px;
    top: 100px;
    width: 1000px;
    height: 700px;
    background: var(--paper);
  }
  .cover__frame {
    position: absolute;
    left: 60px;
    top: 85px;
    right: 60px;
    bottom: 70px;
    border: 1px solid var(--peach-line);
  }
  .cover__panel {
    position: absolute;
    left: 640px;
    top: 40px;
    width: 260px;
    height: 400px;
    background: var(--taupe);
  }
  .cover__panel-rule {
    position: absolute;
    left: 640px;
    top: 85px;
    width: 300px;
    height: 1px;
    background: var(--peach-line);
    opacity: 0.8;
  }
  .cover__photo {
    position: absolute;
    left: 200px;
    top: 170px;
    width: 230px;
    height: 420px;
    background: radial-gradient(ellipse at 50% 60%, var(--stone-mid) 0%, var(--stone-light) 55%, var(--paper) 100%);
  }
  .cover__brand {
    position: absolute;
    right: 100px;
    top: 455px;
    margin: 0;
    font-family: "Cormorant Garamond", Georgia, serif;
    font-weight: 400;
    font-size: 60px;
    line-height: 1;
    letter-spacing: 0.5px;
    color: var(--peach);
  }
</style>
</head>
<body>
  <main class="cover">
    <div class="cover__frame"></div>
    <div class="cover__panel"></div>
    <div class="cover__panel-rule"></div>
    <div class="cover__photo" role="img" aria-label="Photograph of smooth pale stones balanced in a stack"></div>
    <h1 class="cover__brand">Bright Path</h1>
  </main>
</body>
</html>
```